Nutrition-Cooking Website

Hello!
I am in a need of a lovely looking website for my new nutrition practice. I am looking for something sleek, sophisticated, professional yet also welcoming.

Here is a current layout which can be tweaked or overhauled. I feel like the website is not quite what I want so thats why I need your help!!
http://tolvanfolio.example/RENATA-OSSLER-concept-15/

Two websites I like are: (layout similar to www.marquetta.example) or http://www.pernillavostraken.example

Here are the tabs for the website:
About Registered Dietitian Healthy Recipes Philanthropy Shop Features Contact Blog

Features for the Home page include:
Slideshow with 3 rotating updates (like www.marquetta.example)
Video Box (like www.marquetta.example)
Recent Recipes (like http://harrowfield7731.example)
Recent Posts (like http://harrowfield7731.example)
Food Knowledge Box- quick tidbits on laws on food (like www.marquetta.example- she has food wisdom)
Tried and True Benefits of Mediterranean Cuisine (like www.marquetta.example)
Picture of me with brief quote/bio (like www.bettinoruval.example)
Social media buttons

Color Scheme:
• I like the white with gold embroidery or the pretty bluish/purplish in the first pic would be awesome with the slight pink undertones (http://glossedtwirl.example/2012/10/quorvel-marigelle-collection-by-tansley/)
• Also like this goldish background- exotic/sophisticated- http://www.thewhirlingcook.example/Home.html
• Also like the rustic goldish look in the background like this-
ohttp://img.prentlo.example/vexomarks_rsvp_vintage_rustic_gold_swirls_invitation-p161658028764768924bebn6_400.jpg
o http://img.prentlo.example/vexomarks_ornamental_rustic_gold_swirls_invitation-p161776340110432961bvddb_400.jpg
• maybe can have the vines as grapes/olives
OPEN TO ALL DIFFERENT COLORS SCHEMES- whatever looks, clean, sophisticated and professional

Logo:
• Attached is the logo

Budget is flexible. If you think you can improve the website- please do so :)

Target Market(s)

health conscious individuals of all ages

Industry/Entity Type

Embroidery

Requirements
Must have
• clean and sharp look
professional looking
Should not have
• too much busyness

```html
<!DOCTYPE html>
<html lang="en">
<head>
<meta charset="utf-8">
<title>Renata Ossler RD</title>
<link rel="stylesheet" href="https://fonts.googleapis.com/css2?family=Cinzel:wght@400;500&family=Open+Sans:wght@400&family=Arimo:wght@400;700&display=swap">
<style>
:root{
  --page:#e8dcc5;
  --band:#d9ccb4;
  --white:#ffffff;
  --tan:#b19b71;
  --tan-dark:#9e8760;
  --salmon:#e8785c;
  --salmon-text:#d8623f;
  --ink:#222222;
  --ink-soft:#444444;
  --rule:#e6ddd0;
  --footer:#d8c7a3;
}
*{box-sizing:border-box;margin:0;padding:0}
html,body{width:1005px;height:1200px;overflow:hidden}
body{position:relative;background:var(--page);font-family:"Arimo",Arial,sans-serif;color:var(--ink)}
.abs{position:absolute}
.site-header{left:0;top:0;width:1005px;height:122px;background:var(--white)}
.header-rule{left:0;top:122px;width:1005px;height:6px;background:var(--band)}
.logo{left:128px;top:22px;font-family:"Cinzel",serif;font-weight:400;font-size:31px;letter-spacing:1px;color:#1e1e1e;white-space:nowrap}
.social{left:758px;top:26px;display:flex;gap:5px}
.social span{width:26px;height:26px;display:block}
.social .s1{background:#f08a3c}.social .s2{background:#b9c6e2}.social .s3{background:#f1aaa2}.social .s4{background:#a9d8f2}
.main-nav a{position:absolute;top:82px;height:35px;line-height:35px;font-family:"Open Sans",sans-serif;font-size:14px;color:#333;text-decoration:none;white-space:nowrap}
.main-nav a.active{background:var(--salmon);color:#fff;width:64px;text-align:center}
.panel{background:var(--white)}
.photo{display:block}
.display{font-family:"Cinzel",serif;font-weight:400}
.body-copy{font-size:10px;line-height:14px;color:var(--ink)}
.btn{background:var(--tan);color:#fff;font-family:"Cinzel",serif;font-size:12px;letter-spacing:1px;text-align:center}
.hero-caption{left:133px;top:340px;width:476px;height:42px;background:rgba(232,120,92,.82);display:flex;align-items:center;padding-left:15px;font-family:"Open Sans",sans-serif;font-size:12.5px;color:#fff}
.dots{display:flex;gap:4px;margin-right:8px}
.dots i{width:9px;height:9px;border-radius:50%;background:#e0471f;display:block}
.dots i.on{background:#fff}
.arrow{width:30px;height:30px}
.tile-head{left:0;top:0;height:25px;color:#fff;font-size:16px;letter-spacing:1px;text-align:center;line-height:27px}
.tile-cap{height:39px;color:#fff;font-size:11px;line-height:13px;text-align:center;display:flex;align-items:center;justify-content:center}
.list-head{height:36px;color:#fff;font-size:19px;letter-spacing:1px;text-align:center;line-height:38px}
.item-title{font-family:"Cinzel",serif;font-size:12.5px;line-height:15px;color:var(--salmon-text);letter-spacing:.8px}
.item-text{font-size:10px;line-height:14px;text-align:justify;margin-top:5px;color:var(--ink)}
.divider{height:1px;background:var(--rule)}
.box-top{border-top:5px solid var(--tan)}
.tweet{font-size:9px;line-height:14px;color:var(--ink)}
.tweet b{color:var(--salmon-text);font-weight:700}
.site-footer{left:0;top:1168px;width:1005px;height:32px;background:var(--footer);font-size:10px;color:#222}
</style>
</head>
<body>

<header class="abs site-header"></header>
<div class="abs header-rule"></div>
<div class="abs logo">Renata Ossler RD</div>
<div class="abs social" aria-label="Social links"><span class="s1"></span><span class="s2"></span><span class="s3"></span><span class="s4"></span></div>
<nav class="main-nav">
  <a class="active" style="left:122px">Home</a>
  <a style="left:202px">About</a>
  <a style="left:266px">Registered Dietitian</a>
  <a style="left:409px">Healthy Recipes</a>
  <a style="left:532px">Philanthropy</a>
  <a style="left:634px">Shop</a>
  <a style="left:695px">Features</a>
  <a style="left:775px">Contact</a>
  <a style="left:849px">Blog</a>
</nav>

<!-- Hero -->
<section class="abs panel" style="left:126px;top:147px;width:751px;height:243px"></section>
<div class="abs photo" role="img" aria-label="Grilled salmon fillet with lemon slices, asparagus and green salad" style="left:133px;top:155px;width:476px;height:227px;background:linear-gradient(120deg,#f2efe6 0%,#e9d59a 30%,#d98a5a 50%,#8a5a3a 62%,#4f7a3a 80%,#2f4a26 100%)"></div>
<svg class="abs arrow" style="left:140px;top:243px" viewBox="0 0 30 30"><circle cx="15" cy="15" r="13" fill="rgba(255,255,255,.6)" stroke="#555" stroke-width="2"/><path d="M18 9 L10 15 L18 21 Z" fill="#555"/></svg>
<svg class="abs arrow" style="left:575px;top:241px" viewBox="0 0 30 30"><circle cx="15" cy="15" r="13" fill="rgba(255,255,255,.6)" stroke="#555" stroke-width="2"/><path d="M12 9 L20 15 L12 21 Z" fill="#555"/></svg>
<div class="abs hero-caption"><span class="dots"><i></i><i class="on"></i><i></i><i></i></span>One cannot think well, love well, sleep well, if one has not dined well.</div>

<h1 class="abs display" style="left:625px;top:160px;width:240px;text-align:center;font-size:19px;line-height:23px;letter-spacing:1px;color:#1e1e1e">Welcome to Renata Ossler RD</h1>
<div class="abs photo" role="img" aria-label="Black and white portrait of the dietitian in a kitchen" style="left:625px;top:206px;width:236px;height:76px;background:linear-gradient(90deg,#2a2a2a,#6e6e6e 45%,#9a9a9a 55%,#3a3a3a)"></div>
<p class="abs body-copy" style="left:625px;top:292px;width:236px">simply dummy text of the printing and typesetting industry. Lorem Ipsum has been the industry's standard has been the industry's standard&nbsp; text ever since.</p>
<div class="abs btn" style="left:623px;top:355px;width:88px;height:26px;line-height:27px">Read More.</div>

<!-- Feature tiles -->
<section class="abs panel" style="left:126px;top:414px;width:242px;height:209px">
  <div class="abs photo" role="img" aria-label="Assortment of meats, vegetables, fruit, cheese and eggs" style="left:6px;top:7px;width:230px;height:196px;background:linear-gradient(135deg,#a8413a,#d8a24a 40%,#c9c56a 60%,#b8553d)"></div>
  <div class="abs tile-head display" style="left:6px;top:7px;width:230px;background:var(--tan)">Food Philosophy</div>
  <div class="abs tile-cap display" style="left:6px;top:164px;width:230px;background:rgba(177,155,113,.88)">Benefits of all natural foods<br>and the Mediterranean Diet</div>
</section>
<section class="abs panel" style="left:380px;top:414px;width:242px;height:209px">
  <div class="abs photo" role="img" aria-label="Woman choosing between a dessert and a salad, video still" style="left:6px;top:7px;width:230px;height:196px;background:linear-gradient(180deg,#d8c3a4,#b99a76 60%,#8f7356)"></div>
  <svg class="abs" style="left:95px;top:58px" width="52" height="52" viewBox="0 0 52 52"><circle cx="26" cy="26" r="24" fill="rgba(255,255,255,.2)" stroke="#fff" stroke-width="3"/><path d="M20 14 L38 26 L20 38 Z" fill="#fff"/></svg>
  <div class="abs tile-cap display" style="left:6px;top:164px;width:230px;background:rgba(196,180,150,.8);color:#1e1e1e;font-size:14px;line-height:18px">Cooking &amp; Nutrition<br>Videos</div>
</section>
<section class="abs panel" style="left:635px;top:414px;width:242px;height:209px">
  <div class="abs photo" role="img" aria-label="Waiter serving plated dishes at an outdoor garden table" style="left:7px;top:7px;width:229px;height:196px;background:linear-gradient(180deg,#4f6a3a,#8aa06a 40%,#c8c0b0 70%,#b44a3a)"></div>
  <div class="abs tile-head display" style="left:7px;top:7px;width:229px;background:var(--salmon)">Food knowledge</div>
  <div class="abs tile-cap display" style="left:7px;top:164px;width:229px;background:rgba(232,120,92,.9)">Know about the laws and policies<br>affecting our food and nutrition</div>
</section>

<!-- Recent posts -->
<section class="abs panel" style="left:126px;top:646px;width:357px;height:284px">
  <h2 class="abs list-head display" style="left:0;top:0;width:357px;background:var(--tan)">Recent Posts</h2>
  <div class="abs photo" role="img" aria-label="Fruit tartlet with mango and strawberry" style="left:10px;top:48px;width:131px;height:90px;background:linear-gradient(135deg,#f3e3b8,#e8b84a 50%,#d6552f)"></div>
  <div class="abs" style="left:147px;top:49px;width:204px">
    <div class="item-title">Simply dummy text of the print and typesetting</div>
    <p class="item-text">simply dummy text of the printing and typesetting industry. Lorem Ipsum has been the industry's standard dummy text ever since the 1500s.</p>
  </div>
  <div class="abs divider" style="left:7px;top:154px;width:343px"></div>
  <div class="abs photo" role="img" aria-label="Bowl of muesli with strawberries and berries" style="left:10px;top:172px;width:131px;height:90px;background:linear-gradient(135deg,#f3eadf,#e6c79a 40%,#c93a3a 70%,#f2efe8)"></div>
  <div class="abs" style="left:147px;top:173px;width:204px">
    <div class="item-title">Simply dummy text of the print and typesetting</div>
    <p class="item-text">simply dummy text of the printing and typesetting industry. Lorem Ipsum has been the industry's standard dummy text ever since the 1500s.</p>
  </div>
</section>

<!-- Recent recipes -->
<section class="abs panel" style="left:519px;top:646px;width:358px;height:284px">
  <h2 class="abs list-head display" style="left:0;top:0;width:358px;background:var(--salmon)">Recent Recipes</h2>
  <div class="abs photo" role="img" aria-label="Smiling woman holding a bowl of salad" style="left:10px;top:48px;width:131px;height:90px;background:linear-gradient(90deg,#f3f1ee,#5a3a2a 50%,#f3f1ee)"></div>
  <div class="abs" style="left:147px;top:49px;width:204px">
    <div class="item-title">Simply dummy text of the print and typesetting</div>
    <p class="item-text">simply dummy text of the printing and typesetting industry. Lorem Ipsum has been the industry's standard dummy text ever since the 1500s.</p>
  </div>
  <div class="abs divider" style="left:7px;top:154px;width:344px"></div>
  <div class="abs photo" role="img" aria-label="Woman looking into a refrigerator full of fresh food" style="left:10px;top:172px;width:131px;height:90px;background:linear-gradient(180deg,#e8ece9,#c8cfc9 50%,#b04a2a 80%,#6a7a3a)"></div>
  <div class="abs" style="left:147px;top:173px;width:204px">
    <div class="item-title">Simply dummy text of the print and typesetting</div>
    <p class="item-text">simply dummy text of the printing and typesetting industry. Lorem Ipsum has been the industry's standard dummy text ever since the 1500s.</p>
  </div>
</section>

<!-- Newsletter -->
<section class="abs" style="left:126px;top:947px;width:753px;height:48px;background:#e4d6bb;border:1px solid #d3c3a2">
  <h3 class="abs display" style="left:15px;top:10px;font-size:18px;letter-spacing:1px;color:#1e1e1e;white-space:nowrap">Join Renata's Newsletter</h3>
  <div class="abs" style="left:270px;top:11px;width:396px;height:26px;background:var(--white)"></div>
  <div class="abs btn" style="left:666px;top:11px;width:72px;height:26px;line-height:28px;background:#b8a27a">Sign up</div>
</section>

<!-- Tweets -->
<section class="abs panel box-top" style="left:126px;top:1010px;width:364px;height:142px;border-bottom:5px solid var(--tan)">
  <svg class="abs" style="left:10px;top:14px" width="16" height="16" viewBox="0 0 16 16"><circle cx="8" cy="8" r="7" fill="var(--salmon)"/></svg>
  <h3 class="abs display" style="left:32px;top:12px;font-size:15px;letter-spacing:1px;color:var(--salmon-text)">Tweets</h3>
  <div class="abs" style="left:11px;top:44px;width:335px">
    <p class="tweet">Teaching @KBrandtCooks to cook @morningtable at 8:45am....watch if u can!!<br><b>about 7 hours ago</b></p>
    <p class="tweet">Merci Beaucoup @lucvassal “@danrwhitlow: @Miraholtz: @PVostraken @danrwhitlow thanku we had the best time! http://lnk.example/q7Rt2x” <b>about 7 hours ago</b></p>
    <p class="tweet">Only the best for ur bday! “@Miraholtz: dinner at Le Corvelle: purse</p>
  </div>
  <div class="abs" style="left:352px;top:14px;width:4px;height:112px;background:#e9e3da;border-radius:2px"></div>
  <div class="abs" style="left:352px;top:20px;width:5px;height:16px;background:var(--salmon);border-radius:3px"></div>
</section>

<!-- Cooking class -->
<section class="abs panel box-top" style="left:515px;top:1010px;width:364px;height:142px;border-bottom:5px solid var(--tan)">
  <h3 class="abs display" style="left:17px;top:11px;font-size:14.5px;letter-spacing:1px;color:var(--salmon-text);white-space:nowrap">Register for a cooking class</h3>
  <div class="abs photo" role="img" aria-label="Group of people at a cooking class in a kitchen" style="left:18px;top:39px;width:98px;height:78px;background:linear-gradient(135deg,#d9cdb9,#8a6a50 50%,#c9b69a)"></div>
  <p class="abs body-copy" style="left:123px;top:38px;width:228px;text-align:justify">simply dummy text of the printing and typesetting industry. Lorem Ipsum has been the industry's standard dummy text.</p>
  <div class="abs btn" style="left:123px;top:91px;width:100px;height:26px;line-height:27px;font-size:13px">Click Here</div>
</section>

<footer class="abs site-footer">
  <span class="abs" style="left:126px;top:10px">Copyright 2013 Renata Ossler (ACN 318 406 227).</span>
  <span class="abs" style="left:713px;top:11px">Privacy Policy | Terms &amp; Conditions</span>
</footer>

</body>
</html>
```